Vor Business Card

we need a business card for flooring business called Vor Flooring, the design should be black and white. we have 2 locations

Kelmore Showroom
274 Kellaway Road,
Kelmore VIC 3148

Ashvale Showroom
592 Tarrant Hwy,
Ashvale VIC 3192

email : sales@vorflooring.com.au
(03) 9517 2643

Please inform we sell , Laminate, Hybrid, Timber, carpet and commercial flooring

```html
<!DOCTYPE html>
<html lang="en">
<head>
<meta charset="utf-8">
<title>Vor Flooring Business Card</title>
<link href="https://fonts.googleapis.com/css2?family=Poppins:wght@300;400;500&display=swap" rel="stylesheet">
<style>
  :root {
    --backdrop: #e4e4e4;
    --card-dark: #232323;
    --card-light: #f8f8f8;
    --ink-dark: #2a2a2a;
    --ink-light: #ffffff;
    --rule: #1c1c1c;
  }
  * { margin: 0; padding: 0; box-sizing: border-box; }
  html, body { width: 732px; height: 1200px; overflow: hidden; }
  body {
    background: var(--backdrop);
    font-family: "Poppins", sans-serif;
    position: relative;
  }
  .card {
    position: absolute;
    left: 86px;
    width: 560px;
    height: 340px;
    overflow: hidden;
    box-shadow: 0 4px 10px rgba(0,0,0,0.18);
  }
  .card-front { top: 230px; background: var(--card-dark); color: var(--ink-light); }
  .card-back  { top: 630px; background: var(--card-light); color: var(--ink-dark); }

  .brand-name {
    position: absolute;
    font-weight: 400;
    font-size: 24px;
    line-height: 1;
    letter-spacing: 0.5px;
  }
  .card-front .brand-name { left: 30px; top: 44px; color: var(--ink-light); }
  .card-back .brand-name  { left: 30px; top: 106px; color: var(--ink-dark); }
  .brand-name span { display: block; }

  .front-web {
    position: absolute;
    left: 512px;
    top: 22px;
    writing-mode: vertical-rl;
    font-size: 10.5px;
    font-weight: 300;
    letter-spacing: 0.3px;
    line-height: 14px;
  }
  .front-bar {
    position: absolute;
    left: 523px;
    top: 236px;
    width: 3px;
    height: 104px;
    background: var(--ink-light);
  }

  .back-web {
    position: absolute;
    right: 22px;
    top: 18px;
    font-size: 10.5px;
    font-weight: 400;
  }
  .products {
    position: absolute;
    left: 210px;
    top: 110px;
    font-size: 10px;
    font-weight: 400;
    white-space: nowrap;
  }
  .products strong { font-weight: 500; }
  .products-rule {
    position: absolute;
    left: 210px;
    top: 130px;
    width: 332px;
    height: 3px;
    background: var(--rule);
  }
  .showrooms {
    position: absolute;
    left: 425px;
    top: 168px;
    font-size: 10px;
    font-weight: 300;
    line-height: 15px;
    font-style: normal;
  }
  .showroom-divider {
    width: 52px;
    height: 1px;
    background: var(--ink-dark);
    margin: 7px 0 7px;
  }
  .contact {
    position: absolute;
    left: 30px;
    top: 236px;
    font-size: 10px;
    line-height: 15px;
  }
  .contact dt { font-weight: 500; }
  .contact dd { font-weight: 300; margin-bottom: 9px; }
</style>
</head>
<body>
  <section class="card card-front">
    <div class="brand-name"><span>Vor</span><span>Flooring</span></div>
    <div class="front-web">www.vorflooring.com.au</div>
    <div class="front-bar"></div>
  </section>

  <section class="card card-back">
    <div class="back-web">www.vorflooring.com.au</div>
    <div class="brand-name"><span>Vor</span><span>Flooring</span></div>
    <p class="products"><strong>we sell :</strong> Laminate | Hybrid | Timber | carpet | Commercial Flooring</p>
    <div class="products-rule"></div>
    <address class="showrooms">
      Kelmore Showroom<br>274 Kellaway Road,<br>Kelmore VIC 3148
      <div class="showroom-divider"></div>
      Ashvale Showroom<br>592 Tarrant Hwy,<br>Ashvale VIC 3192
    </address>
    <dl class="contact">
      <dt>Phone:</dt><dd>(03) 9517 2643</dd>
      <dt>Email:</dt><dd>sales@vorflooring.com.au</dd>
    </dl>
  </section>
</body>
</html>
```